GLP letterhead

We need a letterhead design for our new company based in Los Angeles called "Gold Lantern Pictures". We develop film and television projects. We work with investors, financiers, film production companies, film distribution and sales companies as well as studios. We would like to incorporate our logo (see attached) but make the letterhead simple and elegant. We need to include: logo, company address, phone number and company website.
Updates

Hello designers, Thanks for your submissions. For our letterhead, we are looking for something more simple and elegant. No heavy bars or lines. Make it feel light and clean. Not a lot of ink on the page. Use the logo and contact info but think "clean", "streamlined" and mostly white paper. Looking forward to seeing more... thanks! Gold Lantern Pictures team

Target Market(s)

Studio executives, talent agents and agencies, financiers, investors.

Industry/Entity Type

It Company

Requirements
Must have
• Gold Lantern Pictures logo (see attached). Logo may be cropped and altered appropriately for elegant letterhead design.
• Please include:
• COMPANY ADDRESS:
• Ridgeway Studio Park
• 2850 Halverson Street
• Tower Annex, 4th Floor
• Manhattan Beach, CA 90412
• COMPANY WEBSITE:
• www.goldlanternpicturesco.example
• COMPANY PHONE NUMBER:
• 310-555-0148

```html
<!DOCTYPE html>
<html lang="en">
<head>
<meta charset="utf-8">
<title>Gold Lantern Pictures Letterhead</title>
<link rel="stylesheet" href="https://fonts.googleapis.com/css2?family=Montserrat:wght@500&family=Roboto+Condensed:wght@500;700&display=swap">
<style>
  :root {
    --backdrop: #e9ebec;
    --paper: #ffffff;
    --ink: #1d1d1f;
    --logo-block: #0a0a0b;
    --accent: #4fa6d6;
    --accent-faint: #dbe9f2;
  }
  html, body {
    margin: 0;
    width: 1200px;
    height: 968px;
    overflow: hidden;
    background: var(--backdrop);
  }
  .letterhead {
    position: absolute;
    left: 290px;
    top: 44px;
    width: 620px;
    height: 880px;
    background: var(--paper);
    box-shadow: 0 2px 10px rgba(0,0,0,0.08);
  }
  .logo-block {
    position: absolute;
    left: 232px;
    top: 0;
    width: 156px;
    height: 112px;
    background: var(--logo-block);
    display: flex;
    flex-direction: column;
    align-items: center;
    justify-content: center;
    gap: 12px;
  }
  .logo-dot {
    width: 22px;
    height: 22px;
    border-radius: 50%;
    background: var(--accent);
  }
  .logo-name {
    font-family: "Montserrat", sans-serif;
    font-weight: 500;
    font-size: 10.5px;
    letter-spacing: 1.6px;
    text-transform: uppercase;
    color: var(--accent);
    text-align: center;
    line-height: 1.35;
  }
  .watermark {
    position: absolute;
    left: 70px;
    top: 230px;
  }
  .contact {
    position: absolute;
    right: 0;
    top: 478px;
    width: 200px;
    font-family: "Roboto Condensed", sans-serif;
    color: var(--ink);
  }
  .contact-rule {
    height: 1.5px;
    background: var(--accent);
    margin-bottom: 10px;
  }
  .contact address {
    font-style: normal;
    font-weight: 500;
    font-size: 10.5px;
    line-height: 1.45;
    padding-left: 22px;
  }
  .contact .web {
    display: block;
    margin-top: 6px;
    font-weight: 700;
  }
  .contact .phone {
    display: block;
    margin-top: 5px;
    font-weight: 700;
    font-size: 17px;
    letter-spacing: 0.3px;
  }
</style>
</head>
<body>
  <main class="letterhead">
    <div class="logo-block">
      <span class="logo-dot"></span>
      <span class="logo-name">Gold Lantern<br>Pictures</span>
    </div>

    <svg class="watermark" width="440" height="440" viewBox="0 0 440 440" aria-hidden="true">
      <circle cx="220" cy="220" r="200" fill="none" stroke="var(--accent-faint)" stroke-width="2"/>
    </svg>

    <section class="contact">
      <div class="contact-rule"></div>
      <address>
        Ridgeway Studio Park<br>
        2850 Halverson Street<br>
        Tower Annex, 4th Floor<br>
        Manhattan Beach<br>
        CA 90412
        <span class="web">www.goldlanternpicturesco.example</span>
        <span class="phone">310-555-0148</span>
      </address>
    </section>
  </main>
</body>
</html>
```